Business card design needed for Renewable utilities company based in New Zealand.

We supply and install solar panels and all components along with it for a fully customisable PV system that helps customer save money on their energy bills right away and also save the planet!

I have attached logo & website design files to give you a better insight.

Industry/Entity Type

Business

```html
<!DOCTYPE html>
<html lang="en">
<head>
<meta charset="utf-8">
<title>Sunward Grid – Business Card</title>
<link rel="stylesheet" href="https://fonts.googleapis.com/css2?family=Raleway:wght@400;500;600&display=swap">
<style>
  :root {
    --stage: #6e6e6e;
    --card: #262424;
    --card-edge: #1c1a1a;
    --text-main: #ffffff;
    --text-soft: #e2e2e2;
    --mark-grey: #8d8d8d;
  }
  * { margin: 0; padding: 0; box-sizing: border-box; }
  html, body { width: 1200px; height: 927px; overflow: hidden; }
  body {
    background: var(--stage);
    font-family: "Raleway", Arial, sans-serif;
    position: relative;
  }
  .card {
    position: absolute;
    background: var(--card);
    box-shadow: 0 0 0 1px var(--card-edge);
  }
  .card--front { left: 86px; top: 75px; width: 624px; height: 359px; }
  .card--back  { left: 326px; top: 477px; width: 576px; height: 366px; }

  .front__name {
    position: absolute; left: 31px; top: 40px;
    font-size: 38px; font-weight: 500; color: var(--text-main);
    letter-spacing: 0.2px;
  }
  .front__tagline {
    position: absolute; left: 31px; top: 96px;
    font-size: 12.5px; color: var(--text-soft);
    display: flex; align-items: center; gap: 14px;
  }
  .front__tagline::before {
    content: ""; width: 8px; height: 8px; border-radius: 50%;
    background: var(--text-main);
  }
  .contact { position: absolute; left: 360px; top: 153px; list-style: none; }
  .contact__item {
    display: flex; align-items: center; gap: 32px;
    font-size: 14px; line-height: 19px; color: var(--text-soft);
    margin-bottom: 9px;
  }
  .contact__icon { width: 26px; height: 26px; flex: none; fill: var(--text-main); }

  .back__brand {
    position: absolute; left: 0; right: 0; top: 92px;
    display: flex; flex-direction: column; align-items: center; gap: 57px;
  }
  .back__dot { width: 96px; height: 96px; border-radius: 50%; background: var(--mark-grey); }
  .back__name {
    font-size: 48px; line-height: 1.2; font-weight: 400; color: var(--mark-grey);
    letter-spacing: 1px;
  }
</style>
</head>
<body>
  <section class="card card--front" aria-label="Card front">
    <h1 class="front__name">Sunward Grid</h1>
    <p class="front__tagline">Cremenu Impsum Mentapentor</p>
    <ul class="contact">
      <li class="contact__item">
        <svg class="contact__icon" viewBox="0 0 24 24" aria-hidden="true"><path d="M12 3 2 12h3v9h5v-6h4v6h5v-9h3z"/></svg>
        <span>42 Kowhai Lane Parnell,<br>Auckland 1052.</span>
      </li>
      <li class="contact__item">
        <svg class="contact__icon" viewBox="0 0 24 24" aria-hidden="true"><path d="M6.6 10.8a15.1 15.1 0 0 0 6.6 6.6l2.2-2.2a1 1 0 0 1 1-.25 11.4 11.4 0 0 0 3.6.57 1 1 0 0 1 1 1V20a1 1 0 0 1-1 1A17 17 0 0 1 3 4a1 1 0 0 1 1-1h3.5a1 1 0 0 1 1 1c0 1.25.2 2.45.57 3.57a1 1 0 0 1-.25 1z"/></svg>
        <span>T:+64 9 555 0142<br>F:+64 9 555 0187</span>
      </li>
      <li class="contact__item">
        <svg class="contact__icon" viewBox="0 0 24 24" aria-hidden="true"><path d="M3 5h18v14H3zm2 2v.5l7 5 7-5V7zm0 3v7h14v-7l-7 5z"/></svg>
        <span>hello.team<br>@sunwardgrid.co</span>
      </li>
      <li class="contact__item">
        <svg class="contact__icon" viewBox="0 0 24 24" aria-hidden="true"><path d="M12 2a10 10 0 1 0 0 20 10 10 0 0 0 0-20zm0 2c.9 0 2.2 1.8 2.8 5H9.2C9.8 5.8 11.1 4 12 4zm-3.2.7A12 12 0 0 0 7.2 9H4.9a8 8 0 0 1 3.9-4.3zm6.4 0A8 8 0 0 1 19.1 9h-2.3a12 12 0 0 0-1.6-4.3zM4.3 11h2.8a16 16 0 0 0 0 2H4.3a8 8 0 0 1 0-2zm4.8 0h5.8a14 14 0 0 1 0 2H9.1a14 14 0 0 1 0-2zm7.8 0h2.8a8 8 0 0 1 0 2h-2.8a16 16 0 0 0 0-2zM4.9 15h2.3a12 12 0 0 0 1.6 4.3A8 8 0 0 1 4.9 15zm4.3 0h5.6c-.6 3.2-1.9 5-2.8 5s-2.2-1.8-2.8-5zm7.6 0h2.3a8 8 0 0 1-3.9 4.3 12 12 0 0 0 1.6-4.3z"/></svg>
        <span>www.sunwardgrid.co</span>
      </li>
    </ul>
  </section>

  <section class="card card--back" aria-label="Card back">
    <div class="back__brand">
      <span class="back__dot" aria-hidden="true"></span>
      <p class="back__name">Sunward Grid</p>
    </div>
  </section>
</body>
</html>
```